Clean professional business card design

Need a professional looking, high quality card and letterhead design. Business card would prefer to have a grey tone to the background.

Back of card needs to have: "Securities offered through Norvane Capital Partners LLC (doing Insurance business in CA as NKPTR Insurance Agency), member BRAXEL/TOVMA. Advisory services offered through Norvane Wealth Counsel LLC. Norvane entities are under separate ownership from any other named entity. [employee name] CA Insurance Lic #7K21904

Industry/Entity Type

Financial Planning

Font styles to use
Serif
Sans Serif

Requirements
Must have
• Customization of text so that I can adjust for other employee

```html
<!DOCTYPE html>
<html lang="en">
<head>
<meta charset="utf-8">
<title>Keystead Financial Advisers – Business Card</title>
<link href="https://fonts.googleapis.com/css2?family=Cinzel:wght@500&family=Roboto+Condensed:wght@400;700&display=swap" rel="stylesheet">
<style>
  :root {
    --page-bg: #ece9e4;
    --card-front: #ffffff;
    --card-back: #a9a9a9;
    --brand-blue: #1a73c9;
    --text-grey: #8e8e8e;
    --text-dark: #3a3a3a;
    --rule: #bdbdbd;
    --white: #ffffff;
  }
  * { margin: 0; padding: 0; box-sizing: border-box; }
  html, body { width: 1200px; height: 911px; overflow: hidden; }
  body {
    background: var(--page-bg);
    font-family: "Roboto Condensed", Arial, sans-serif;
    position: relative;
  }
  .card {
    position: absolute;
    top: 307px;
    width: 520px;
    height: 297px;
    box-shadow: 0 6px 18px rgba(0,0,0,0.18);
  }
  .card--front { left: 50px; background: var(--card-front); }
  .card--back { left: 630px; background: var(--card-back); }

  .brand {
    display: flex;
    align-items: center;
    gap: 12px;
    color: var(--brand-blue);
    font-family: "Cinzel", Georgia, serif;
    font-weight: 500;
  }
  .brand__mark { width: 22px; height: 22px; background: var(--brand-blue); flex: none; }
  .brand__name { font-size: 22px; line-height: 1.15; letter-spacing: 0.5px; }

  .card--front .brand { position: absolute; left: 40px; top: 112px; width: 215px; }
  .divider {
    position: absolute; left: 275px; top: 0; bottom: 0;
    width: 1px; background: var(--rule);
  }
  .person { position: absolute; left: 300px; top: 38px; right: 24px; }
  .person__name {
    color: var(--brand-blue); font-weight: 700; font-size: 17px; letter-spacing: 0.3px;
  }
  .person__title { color: var(--text-grey); font-size: 12px; margin-top: 2px; }
  .person__rule { height: 1px; width: 120px; background: var(--text-dark); margin: 10px 0 12px; }
  .address { color: var(--text-dark); font-size: 12.5px; line-height: 1.4; }
  .contacts { list-style: none; margin-top: 16px; }
  .contacts li {
    display: flex; align-items: center; gap: 8px;
    color: var(--text-dark); font-size: 12.5px; line-height: 1.55;
  }
  .contacts svg { width: 11px; height: 11px; fill: var(--brand-blue); flex: none; }

  .card--back .brand { position: absolute; left: 140px; top: 62px; width: 260px; }
  .card--back .brand__name { font-size: 25px; }
  .disclaimer {
    position: absolute; left: 36px; right: 36px; bottom: 34px;
    color: var(--white); font-size: 11px; line-height: 1.45; text-align: left;
  }
</style>
</head>
<body>
  <section class="card card--front" aria-label="Business card front">
    <div class="brand">
      <span class="brand__mark"></span>
      <span class="brand__name">Keystead Financial Advisers</span>
    </div>
    <div class="divider"></div>
    <div class="person">
      <div class="person__name">DANIEL REYES</div>
      <div class="person__title">CEO/FOUNDER</div>
      <div class="person__rule"></div>
      <p class="address">4120 Larkfield Road<br>Fairbrook, Alaska 99817</p>
      <ul class="contacts">
        <li><svg viewBox="0 0 12 12"><path d="M2.5 1 L4.5 1 L5.3 3.5 L4 4.6 C4.7 6 6 7.3 7.4 8 L8.5 6.7 L11 7.5 L11 9.5 C11 10.3 10.3 11 9.5 11 C5 11 1 7 1 2.5 C1 1.7 1.7 1 2.5 1 Z"/></svg>555 014 2276</li>
        <li><svg viewBox="0 0 12 12"><path d="M3 0.5 H9 V11.5 H3 Z M4 1.8 V9 H8 V1.8 Z"/></svg>555 019 8342</li>
        <li><svg viewBox="0 0 12 12"><path d="M3 1 H8 V4 H3 Z M1 4.5 H11 V10 H1 Z"/></svg>555 016 4503</li>
        <li><svg viewBox="0 0 12 12"><path d="M1 2.5 H11 V9.5 H1 Z M1.6 3 L6 6.5 L10.4 3 Z" fill-rule="evenodd"/></svg>name@keysteadfa.com</li>
        <li><svg viewBox="0 0 12 12"><circle cx="6" cy="6" r="5"/></svg>www.keysteadfa.com</li>
      </ul>
    </div>
  </section>

  <section class="card card--back" aria-label="Business card back">
    <div class="brand">
      <span class="brand__mark"></span>
      <span class="brand__name">Keystead Financial Advisers</span>
    </div>
    <p class="disclaimer">Securities offered through Norvane Capital Partners LLC (doing Insurance business in CA as NKPTR Insurance Agency), member BRAXEL/TOVMA. Advisory services offered through Norvane Wealth Counsel LLC. Norvane entities are under separate ownership from any other named entity. [employee name] CA Insurance Lic #7K21904</p>
  </section>
</body>
</html>
```